CD cover for "Gold Lanterns" Song by Hip Hop Artist Mavro47

Need a raphic design for a new song on a mixtape . it needs to incorporate the artist logo, the record label logo, and the explicit language warning on the cover as well. "Gold Lanterns" are a sexy brand designer shoes by Benedikt Sarrazol and prefered by Hot and Sexy women of today. So the cover needs to reflect that

```html
<!DOCTYPE html>
<html lang="en">
<head>
<meta charset="utf-8">
<title>Gold Lanterns – Mavro47</title>
<link rel="stylesheet" href="https://fonts.googleapis.com/css2?family=Josefin+Sans:wght@300;400;600&family=Anton&display=swap">
<style>
  :root {
    --stage: #5a5a5a;
    --paper: #f7f4f5;
    --paper-shade: #ebe7e8;
    --floor: #fbf8f9;
    --ink: #1c1c1e;
    --lacquer: #d3101c;
    --skin-light: #e9bfa6;
    --skin-deep: #d39c80;
    --heel: #dd2a27;
  }
  html, body {
    margin: 0;
    padding: 0;
    width: 1200px;
    height: 603px;
    overflow: hidden;
    background: var(--stage);
  }
  .cover {
    position: absolute;
    left: 320px;
    top: 21px;
    width: 560px;
    height: 560px;
    overflow: hidden;
    background: linear-gradient(180deg, var(--paper) 0%, var(--paper-shade) 62%, var(--floor) 62.4%, var(--floor) 100%);
  }
  .cover__photo {
    position: absolute;
    right: 0;
    top: 0;
    width: 250px;
    height: 470px;
    background:
      linear-gradient(180deg, rgba(233,191,166,0.85) 0%, rgba(211,156,128,0.75) 55%, rgba(221,42,39,0.85) 78%, rgba(221,42,39,0.55) 100%);
    opacity: 0.55;
  }
  .title {
    position: absolute;
    left: 22px;
    top: 248px;
    margin: 0;
    font-family: "Josefin Sans", sans-serif;
    line-height: 0.86;
    letter-spacing: 1px;
  }
  .title__accent {
    display: block;
    color: var(--lacquer);
    font-weight: 600;
    font-size: 74px;
  }
  .title__main {
    display: block;
    color: var(--ink);
    font-weight: 300;
    font-size: 66px;
  }
  .artist {
    position: absolute;
    left: 22px;
    top: 500px;
    margin: 0;
    font-family: "Anton", sans-serif;
    font-size: 34px;
    line-height: 1;
    color: var(--ink);
    letter-spacing: 0.5px;
  }
  .label {
    position: absolute;
    right: 24px;
    top: 508px;
    display: flex;
    align-items: center;
    gap: 7px;
    font-family: "Josefin Sans", sans-serif;
    font-weight: 600;
    font-size: 17px;
    color: var(--ink);
    letter-spacing: 1px;
    text-transform: uppercase;
  }
  .label__mark {
    width: 14px;
    height: 14px;
    background: var(--ink);
  }
</style>
</head>
<body>
  <main class="cover">
    <div class="cover__photo" role="img" aria-label="Photograph of a woman's legs stepping in glossy red stiletto heels against a pale textured wall"></div>
    <h1 class="title">
      <span class="title__accent">GOLD</span>
      <span class="title__main">LANTERNS</span>
    </h1>
    <p class="artist">MAVRO47</p>
    <div class="label">
      <span class="label__mark"></span>
      <span class="label__name">Brickvine Music</span>
    </div>
  </main>
</body>
</html>
```